Membership Based Medical Practice Website

We need a functioning website for a new Membership based medical practice. There will be an enrollment fee and a monthly fee. We would like to see designs that are modern, simple. Should use neutral light colors. Examples of sites we like are www.fenmorlaclinic.com and https://healerneartheknoll.com/ We also have a link that when "Join Now" is clicked it will go to the signup website.

Target Market(s)

Gay Men, local population, Age group 20 to 60's.

Industry/Entity Type

Medical

Coding

Coded - Design and coding required

Number of Pages Required

5+ page

Font styles to use
Sans Serif

Colors
ffffff
cee9f5
ecf7fb
cfeae6
edf8f6
aaaaaa
e9e9e9
dbdbdb
fff3d1

Requirements
Must have
• Logo and header on every page. Clean, simple design, clear content, mobile compatible.
• Must use Wordpress
Nice to have
• Ideas should come from fenmorlaclinic.com
• Easy to read
Should not have
• Generic patient pictures, bold colors.
• Should not copy from above websites.

```html
<!DOCTYPE html>
<html lang="en">
<head>
<meta charset="utf-8">
<title>Larkmoor Infectious Disease Specialists</title>
<link href="https://fonts.googleapis.com/css2?family=Lato:wght@300;400;700;900&display=swap" rel="stylesheet">
<style>
:root{
  --white:#ffffff;
  --ink:#2b2b2b;
  --ink-soft:#3d3d3d;
  --muted:#aaaaaa;
  --line:#e9e9e9;
  --sky-band:#ecf7fb;
  --mint:#cfeae6;
  --mint-band:#edf8f6;
  --cream:#fff3d1;
  --teal:#1a9cc8;
  --gold:#c9a35a;
}
*{margin:0;padding:0;box-sizing:border-box}
html,body{width:1200px;height:2736px;overflow:hidden;background:var(--white)}
body{font-family:"Lato",sans-serif;color:var(--ink);position:relative}

/* header */
.site-header{position:absolute;left:0;top:0;width:1200px;height:142px;background:var(--white)}
.brand{position:absolute;left:73px;top:30px;width:200px;text-align:center}
.brand-mark{width:40px;height:40px;border-radius:50%;border:2px solid var(--gold);margin:0 auto 14px}
.brand-name{font-size:15px;letter-spacing:11px;color:var(--ink-soft);font-weight:400;padding-left:11px}
.brand-tag{font-size:10.5px;letter-spacing:.4px;color:var(--ink-soft);margin-top:3px}
.main-nav{position:absolute;top:67px;left:443px;display:flex;gap:41px;white-space:nowrap}
.main-nav a{font-size:14px;font-weight:700;color:var(--ink-soft);text-decoration:none;letter-spacing:.2px}
.btn-join{position:absolute;left:1007px;top:55px;width:118px;height:43px;border-radius:22px;background:var(--mint);color:var(--ink);font-weight:700;font-size:15px;display:flex;align-items:center;justify-content:center;letter-spacing:.5px;text-decoration:none}

/* hero */
.hero{position:absolute;left:0;top:142px;width:1200px;height:537px;background:linear-gradient(180deg,#cfd4d2 0%,#8f9a8f 30%,#4f6148 48%,#2c2f2e 70%,#1e1f20 100%)}
.hero-title{position:absolute;left:0;top:222px;width:1200px;text-align:center;color:var(--white);font-weight:900;font-size:38px;line-height:42px;text-shadow:0 1px 3px rgba(0,0,0,.35)}
.hero-dots{position:absolute;top:486px;left:555px;display:flex;gap:12px}
.hero-dots span{width:14px;height:14px;border-radius:50%;background:var(--white)}
.hero-dots span.on{background:var(--mint)}

/* specialties */
.specialties{position:absolute;left:0;top:679px;width:1200px;height:479px;background:var(--sky-band)}
.section-lead{text-align:center;font-weight:300;font-size:34px;line-height:41px;color:var(--ink-soft)}
.section-sub{text-align:center;font-size:23px;color:var(--ink);margin-top:10px}
.specialties .section-lead{padding-top:56px}
.spec-list{position:absolute;list-style:none;top:216px}
.spec-list li{display:flex;align-items:center;font-size:19px;color:var(--teal);height:42px;white-space:nowrap}
.spec-list svg{width:18px;height:18px;margin-right:17px;flex:none}
.spec-left{left:252px}
.spec-right{left:681px}

/* features */
.features{position:absolute;left:0;top:1158px;width:1200px;height:863px}
.features .section-lead{padding-top:52px;font-size:33px}
.features .section-sub{margin-top:8px}
.feature-grid{position:absolute;left:58px;top:174px;width:1084px;display:grid;grid-template-columns:repeat(4,271px)}
.feature{height:305px;text-align:center;padding-top:32px;border-left:1px solid var(--line)}
.feature:nth-child(4n+1){border-left:none}
.feature.row-two{border-top:1px solid var(--line);height:315px;padding-top:58px}
.feature-icon{width:80px;height:80px;border-radius:50%;background:var(--cream);margin:0 auto;display:flex;align-items:center;justify-content:center}
.feature-icon svg{width:40px;height:40px}
.feature h3{font-size:18px;font-weight:700;margin-top:22px;color:var(--ink)}
.feature p{font-size:14.5px;line-height:26px;color:var(--ink-soft);margin:8px auto 0;width:250px}

/* pricing */
.pricing{position:absolute;left:0;top:2021px;width:1200px;height:511px;background:var(--mint-band)}
.pricing-photo{position:absolute;left:0;top:0;width:587px;height:511px;background:radial-gradient(ellipse at 45% 45%,#e9e7e2 0%,#b9b4ad 22%,#7a2b2b 48%,#3a1d1f 80%,#241518 100%)}
.pricing-body{position:absolute;left:620px;top:40px;width:540px}
.pricing-body h2{font-weight:400;font-size:31px;line-height:40px;color:var(--ink-soft)}
.plan{font-size:19px;line-height:27px;margin-top:14px;color:var(--ink)}
.perks{list-style:none;margin-top:18px}
.perks li{display:flex;align-items:flex-start;font-size:15.5px;line-height:24px;color:var(--ink-soft);margin-bottom:6px}
.perks svg{width:14px;height:14px;margin:5px 15px 0 0;flex:none}
.btn-learn{display:flex;align-items:center;justify-content:center;width:242px;height:43px;border-radius:22px;background:var(--mint);font-weight:700;font-size:16px;color:var(--ink);margin-top:38px;margin-left:-3px;text-decoration:none}

/* footer */
.site-footer{position:absolute;left:0;top:2532px;width:1200px;height:204px;text-align:center}
.foot-nav{display:flex;justify-content:center;padding-top:59px}
.foot-nav a{font-size:14px;font-weight:700;color:var(--ink-soft);text-decoration:none;letter-spacing:.3px;margin:0 23px}
.copyright{font-size:13px;color:var(--ink-soft);margin-top:14px}
.social{display:flex;justify-content:center;gap:20px;margin-top:16px}
.social span{width:18px;height:18px;border-radius:50%;background:#777777}
</style>
</head>
<body>

<header class="site-header">
  <div class="brand">
    <div class="brand-mark"></div>
    <div class="brand-name">LARKMOOR</div>
    <div class="brand-tag">INFECTIOUS DISEASE SPECIALISTS</div>
  </div>
  <nav class="main-nav">
    <a href="#">HOME</a><a href="#">SPECIALTIES</a><a href="#">PRICING</a><a href="#">ABOUT US</a><a href="#">FAQ</a><a href="#">BLOG</a>
  </nav>
  <a class="btn-join" href="#">JOIN US</a>
</header>

<section class="hero" role="img" aria-label="Photograph of an empty road stretching through green fields toward misty hills">
  <h1 class="hero-title">Specialty medicine with Commitment,<br>Compassion and Care</h1>
  <div class="hero-dots"><span class="on"></span><span></span><span></span><span></span></div>
</section>

<section class="specialties">
  <h2 class="section-lead">We offer comprehensive treatment of a wide<br>variety of infectious diseases.</h2>
  <p class="section-sub">Out expertise is in the following area.</p>
  <ul class="spec-list spec-left">
    <li><svg viewBox="0 0 18 18"><circle cx="9" cy="9" r="9" fill="#1a9cc8"/><path d="M5 9.3l2.7 2.6L13 6.5" stroke="#fff" stroke-width="2.2" fill="none"/></svg>HIV/PrEP</li>
    <li><svg viewBox="0 0 18 18"><circle cx="9" cy="9" r="9" fill="#1a9cc8"/><path d="M5 9.3l2.7 2.6L13 6.5" stroke="#fff" stroke-width="2.2" fill="none"/></svg>Chronic Hepatitis</li>
    <li><svg viewBox="0 0 18 18"><circle cx="9" cy="9" r="9" fill="#1a9cc8"/><path d="M5 9.3l2.7 2.6L13 6.5" stroke="#fff" stroke-width="2.2" fill="none"/></svg>Sexually transmitted infections</li>
    <li><svg viewBox="0 0 18 18"><circle cx="9" cy="9" r="9" fill="#1a9cc8"/><path d="M5 9.3l2.7 2.6L13 6.5" stroke="#fff" stroke-width="2.2" fill="none"/></svg>Pre-travel vaccinations and counselling</li>
    <li><svg viewBox="0 0 18 18"><circle cx="9" cy="9" r="9" fill="#1a9cc8"/><path d="M5 9.3l2.7 2.6L13 6.5" stroke="#fff" stroke-width="2.2" fill="none"/></svg>Infections associated with medical devices</li>
  </ul>
  <ul class="spec-list spec-right">
    <li><svg viewBox="0 0 18 18"><circle cx="9" cy="9" r="9" fill="#1a9cc8"/><path d="M5 9.3l2.7 2.6L13 6.5" stroke="#fff" stroke-width="2.2" fill="none"/></svg>Bone and Joint infections</li>
    <li><svg viewBox="0 0 18 18"><circle cx="9" cy="9" r="9" fill="#1a9cc8"/><path d="M5 9.3l2.7 2.6L13 6.5" stroke="#fff" stroke-width="2.2" fill="none"/></svg>Postsurgical infections</li>
    <li><svg viewBox="0 0 18 18"><circle cx="9" cy="9" r="9" fill="#1a9cc8"/><path d="M5 9.3l2.7 2.6L13 6.5" stroke="#fff" stroke-width="2.2" fill="none"/></svg>Diabetes related infections</li>
    <li><svg viewBox="0 0 18 18"><circle cx="9" cy="9" r="9" fill="#1a9cc8"/><path d="M5 9.3l2.7 2.6L13 6.5" stroke="#fff" stroke-width="2.2" fill="none"/></svg>Tuberculosis</li>
  </ul>
</section>

<section class="features">
  <h2 class="section-lead">Less wait, more personal.</h2>
  <p class="section-sub">We are not your traditional doctor’s office.</p>
  <div class="feature-grid">
    <div class="feature">
      <div class="feature-icon"><svg viewBox="0 0 40 40"><text x="20" y="31" text-anchor="middle" font-family="Lato,sans-serif" font-weight="900" font-size="32" fill="#2b2b2b">$</text></svg></div>
      <h3>Straightforward pricing</h3>
      <p>We charge all our patients thesame low rate - no surprises.</p>
    </div>
    <div class="feature">
      <div class="feature-icon"><svg viewBox="0 0 40 40"><path d="M20 4c-6.6 0-12 5.2-12 11.8C8 24.5 20 36 20 36s12-11.5 12-20.2C32 9.2 26.6 4 20 4z" fill="#2b2b2b"/><circle cx="20" cy="15.5" r="4.5" fill="#fff3d1"/></svg></div>
      <h3>Available when you are</h3>
      <p>New patient appointments are available within 1 week.</p>
    </div>
    <div class="feature">
      <div class="feature-icon"><svg viewBox="0 0 40 40"><rect x="5" y="8" width="30" height="27" rx="2" fill="#2b2b2b"/><rect x="11" y="4" width="3" height="7" fill="#2b2b2b"/><rect x="26" y="4" width="3" height="7" fill="#2b2b2b"/><g fill="#fff3d1"><rect x="9" y="16" width="4" height="4"/><rect x="15" y="16" width="4" height="4"/><rect x="21" y="16" width="4" height="4"/><rect x="27" y="16" width="4" height="4"/><rect x="9" y="22" width="4" height="4"/><rect x="15" y="22" width="4" height="4"/><rect x="21" y="22" width="4" height="4"/><rect x="27" y="22" width="4" height="4"/><rect x="9" y="28" width="4" height="4"/><rect x="15" y="28" width="4" height="4"/><rect x="21" y="28" width="4" height="4"/></g></svg></div>
      <h3>Hassle-free booking</h3>
      <p>Schedule your appointment online at your convenience - no need to call during business hours.</p>
    </div>
    <div class="feature">
      <div class="feature-icon"><svg viewBox="0 0 40 40"><path d="M20 22c-4-3.5-9-7-9-11.5 0-3 2.3-5 4.8-5 1.8 0 3.3 1 4.2 2.4.9-1.4 2.4-2.4 4.2-2.4 2.5 0 4.8 2 4.8 5C29 15 24 18.5 20 22z" fill="#2b2b2b"/><path d="M4 16l5 9 8 4v7h-4v-4l-7-4-3-10zM36 16l-5 9-8 4v7h4v-4l7-4 3-10z" fill="#2b2b2b"/></svg></div>
      <h3>Devoted care</h3>
      <p>We schedule enough time at each visit to make sure all of your questions are answered.</p>
    </div>
    <div class="feature row-two">
      <div class="feature-icon"><svg viewBox="0 0 40 40"><rect x="5" y="11" width="21" height="18" rx="3" fill="#2b2b2b"/><path d="M27 17l9-5v16l-9-5z" fill="#2b2b2b"/></svg></div>
      <h3>Within your reach</h3>
      <p>Follow-up appointments may be done by video chat for your convenience.</p>
    </div>
    <div class="feature row-two">
      <div class="feature-icon"><svg viewBox="0 0 40 40"><path d="M15 5h10v2h-2v9l9 15c1 2-.2 4-2.4 4H10.4C8.2 35 7 33 8 31l9-15V7h-2z" fill="none" stroke="#2b2b2b" stroke-width="2.4"/><path d="M12 26h16l3.5 6H8.5z" fill="#2b2b2b"/></svg></div>
      <h3>Save on lab costs</h3>
      <p>If paying upfront for labs, we offer discounted pricing of up to 90% off standard rates.</p>
    </div>
    <div class="feature row-two">
      <div class="feature-icon"><svg viewBox="0 0 40 40"><path d="M20 31C13 25 4 20 4 12.5 4 8 7.5 5 11.5 5c3.5 0 6.3 2 8.5 5 2.2-3 5-5 8.5-5C32.5 5 36 8 36 12.5c0 2-.6 3.8-1.6 5.5" fill="#2b2b2b"/><path d="M7 17h6l2-4 3 8 2-4h5" stroke="#fff3d1" stroke-width="2" fill="none"/><circle cx="29" cy="28" r="8" fill="#2b2b2b" stroke="#fff3d1" stroke-width="2"/><path d="M29 23.5V28l3 2" stroke="#fff3d1" stroke-width="2" fill="none"/></svg></div>
      <h3>Save on medications</h3>
      <p>We offer deeply discounted wholesale price medications for<br>our members at pharmacy<br>on site.</p>
    </div>
    <div class="feature row-two">
      <div class="feature-icon"><svg viewBox="0 0 40 40"><circle cx="20" cy="12" r="7.5" fill="#2b2b2b"/><path d="M6 35c0-8 6-13 14-13s14 5 14 13z" fill="#2b2b2b"/></svg></div>
      <h3>No middle man</h3>
      <p>We don’t bill any insurance plans so decisions about your healthcare will be made by you and Dr. Halvorsen, without the impersonal management that comes from third-party payers.</p>
    </div>
  </div>
</section>

<section class="pricing">
  <div class="pricing-photo" role="img" aria-label="Photograph of a hand in a red sweater holding an enamel camping mug filled with snow"></div>
  <div class="pricing-body">
    <h2>Our pricing is simple, transparent<br>and affordable.</h2>
    <p class="plan">Membership Plan $80/mo, plus a one-time<br>$99 enrollment fee.</p>
    <ul class="perks">
      <li><svg viewBox="0 0 18 18"><circle cx="9" cy="9" r="9" fill="#1a9cc8"/><path d="M5 9.3l2.7 2.6L13 6.5" stroke="#fff" stroke-width="2.4" fill="none"/></svg>Includes all appointments, no co-pay</li>
      <li><svg viewBox="0 0 18 18"><circle cx="9" cy="9" r="9" fill="#1a9cc8"/><path d="M5 9.3l2.7 2.6L13 6.5" stroke="#fff" stroke-width="2.4" fill="none"/></svg>Relaxed, unrushed visits</li>
      <li><svg viewBox="0 0 18 18"><circle cx="9" cy="9" r="9" fill="#1a9cc8"/><path d="M5 9.3l2.7 2.6L13 6.5" stroke="#fff" stroke-width="2.4" fill="none"/></svg>Direct communication with your doctor via phone, email,<br>video chat 24/7</li>
      <li><svg viewBox="0 0 18 18"><circle cx="9" cy="9" r="9" fill="#1a9cc8"/><path d="M5 9.3l2.7 2.6L13 6.5" stroke="#fff" stroke-width="2.4" fill="none"/></svg>Convenient online scheduling (no need to call during business hours)</li>
      <li><svg viewBox="0 0 18 18"><circle cx="9" cy="9" r="9" fill="#1a9cc8"/><path d="M5 9.3l2.7 2.6L13 6.5" stroke="#fff" stroke-width="2.4" fill="none"/></svg>Wholesale price for labs and medications</li>
    </ul>
    <a class="btn-learn" href="#">Learn More About Us</a>
  </div>
</section>

<footer class="site-footer">
  <nav class="foot-nav">
    <a href="#">HOME</a><a href="#">SPECIALTIES</a><a href="#">PRICING</a><a href="#">ABOUT US</a><a href="#">FAQ</a><a href="#">BLOG</a>
  </nav>
  <p class="copyright">Copyright © 2019 CompanyName All Rights Reserved.</p>
  <div class="social" aria-label="Social links"><span></span><span></span><span></span><span></span><span></span></div>
</footer>

</body>
</html>
```